Harbor LunaVital & Equipments

I need to create full stationery design for the company; Business Card, Envelop, Letterheads, Calendar and email template.

Our company is specialized in the import and export of nutritional, pharmaceutical and cosmetics in addition to medical equipments.

These is no limitation on how to use colors within the design.

Target Market(s)

Global

Industry/Entity Type

Healthcare

Other font styles liked:
• a font close to logo. Letterhead body text to be different than the address text

Requirements
Nice to have
• We will have multiple locations so it is good to keep space for future addresses.
• Stationary requirements:
• Letterhead: A4
• Envelopes: 3 regular sizes : large, medium and small (i do not know the sizes)
• Colors: extracted from the logo

```html
<!DOCTYPE html>
<html lang="en">
<head>
<meta charset="utf-8">
<title>Harbor LunaVital &amp; Equipments — Business Card</title>
<link rel="stylesheet" href="https://fonts.googleapis.com/css2?family=PT+Sans:wght@400;700&display=swap">
<style>
  :root {
    --navy: #050a5a;
    --cyan: #29abe2;
    --green: #22a31f;
    --orange: #fbb034;
    --white: #ffffff;
    --ink-grey: #555555;
    --page: #e9e9e9;
  }
  * { box-sizing: border-box; margin: 0; padding: 0; }
  html, body { width: 1105px; height: 1200px; overflow: hidden; }
  body {
    background: var(--page);
    font-family: "PT Sans", sans-serif;
    position: relative;
  }
  .card {
    position: absolute;
    left: 192px;
    width: 720px;
    height: 410px;
    border-radius: 22px;
    overflow: hidden;
  }
  .card-front { top: 166px; background: var(--navy); color: var(--white); }
  .card-back { top: 624px; background: var(--white); }

  .holder-name {
    position: absolute; left: 38px; top: 36px;
    font-size: 27px; font-weight: 700; color: var(--cyan);
  }
  .holder-title {
    position: absolute; left: 38px; top: 68px;
    font-size: 19px; color: var(--green);
  }
  .address {
    position: absolute; left: 38px;
    font-size: 19px; line-height: 27px;
  }
  .address-one { top: 126px; }
  .address-two { top: 184px; }
  .contact-list {
    position: absolute; left: 38px; top: 244px;
    list-style: none;
    font-size: 19px; line-height: 28px;
  }
  .contact-list li { display: flex; align-items: center; gap: 10px; }
  .contact-icon { width: 17px; height: 17px; flex: none; }

  .brand-block {
    position: absolute; left: 420px; top: 0; width: 300px; height: 410px;
    display: flex; align-items: center; justify-content: center; gap: 14px;
  }
  .brand-mark {
    width: 22px; height: 22px; background: var(--cyan); border-radius: 4px; flex: none;
  }
  .brand-name {
    font-size: 28px; font-weight: 700; line-height: 34px; color: var(--white);
  }

  .back-brand {
    position: absolute; left: 0; top: 150px; width: 100%;
    display: flex; align-items: center; justify-content: center; gap: 14px;
  }
  .back-brand .brand-mark { background: var(--cyan); }
  .back-brand .brand-name { color: var(--navy); font-size: 32px; }
  .back-web {
    position: absolute; left: 0; top: 338px; width: 100%;
    text-align: center;
    font-size: 19px; letter-spacing: 4px; color: var(--ink-grey);
  }
</style>
</head>
<body>
  <section class="card card-front">
    <h1 class="holder-name">Daniel Reeve</h1>
    <p class="holder-title">CEO/Founder</p>

    <p class="address address-one">4210 Cedarwood Court<br>Juneau, Alaska 99801</p>
    <p class="address address-two">1296 Harborview Road<br>Garden Hills, NY 11040</p>

    <ul class="contact-list">
      <li>
        <svg class="contact-icon" viewBox="0 0 24 24" aria-hidden="true"><path fill="#29abe2" d="M6.6 10.8a15.1 15.1 0 0 0 6.6 6.6l2.2-2.2c.3-.3.7-.4 1-.2 1.1.4 2.3.6 3.6.6.6 0 1 .4 1 1V20c0 .6-.4 1-1 1A17 17 0 0 1 3 4c0-.6.4-1 1-1h3.5c.6 0 1 .4 1 1 0 1.3.2 2.5.6 3.6.1.3 0 .7-.2 1l-2.3 2.2z"/></svg>
        <span>555 214 7730</span>
      </li>
      <li>
        <svg class="contact-icon" viewBox="0 0 24 24" aria-hidden="true"><path fill="#29abe2" d="M6 3h12v5H6zM3 9h18a1 1 0 0 1 1 1v7h-4v4H6v-4H2v-7a1 1 0 0 1 1-1zm5 7v3h8v-3z"/></svg>
        <span>555 380 6192</span>
      </li>
      <li>
        <svg class="contact-icon" viewBox="0 0 24 24" aria-hidden="true"><path fill="#29abe2" d="M2 5h20v14H2zm2 2v.5l8 5 8-5V7l-8 5z"/></svg>
        <span>hello@harborluna.com</span>
      </li>
      <li>
        <svg class="contact-icon" viewBox="0 0 24 24" aria-hidden="true"><circle cx="12" cy="12" r="10" fill="#29abe2"/><path fill="#050a5a" d="M8 6c2 1 3 2 2 4s-3 1-3 3 2 3 1 5c-2-1-4-3-4-6 0-3 2-5 4-6zm8 3c2 0 3 2 2 4-1 1-3 0-3 2s1 3 0 4c-1 0-2-2-2-4s1-6 3-6z"/></svg>
        <span>www.harborluna.com</span>
      </li>
    </ul>

    <div class="brand-block">
      <span class="brand-mark"></span>
      <p class="brand-name">Harbor LunaVital<br>&amp; Equipments</p>
    </div>
  </section>

  <section class="card card-back">
    <div class="back-brand">
      <span class="brand-mark"></span>
      <p class="brand-name">Harbor LunaVital &amp; Equipments</p>
    </div>
    <p class="back-web">www.harborluna.com</p>
  </section>
</body>
</html>
```